VORELT B2B portal design
Fantastic design work, top communication and fast design changes! Many thanks,Jens & Uwe from VORELT
Zielgruppe
We are a B2B Cloud Services StartUp that creates B2B logistics & supply chain processes between customer and its suppliers.
Aufgabenstellung
We need a modern responsive able design, that should consider that we are NOT presenting goods or clothes or similar on the portal pages but we show mainly data grids, kpi dashboards, forms, and setting panels to our customer and their suppliers.
The design must be clean and straight not to distract people from the important information in these data grids, kpi dashboards, forms, and settings panels.
We need our logo perfectly embedded and the pages coloured around from grey to blue.
The Designer must be able to deliver a design and transfer it to a highly responsive HTML (5) template (without technical content or further functionality). This our programmers will implement afterwards in .Net.
We need in total 3 page templates:
1. Login Page
2. Main Page with overview over the following services text (each one shown in one tile)
"ZMS (Time Frame Management)"
"DMS (Document Management)"
"REMS (Reporting Management)"
-> Note: At the end we will have up to 12 or more tiles (services) so the design should be additive
3. Data grid (e.g. list of customers)/form (e.g. customer registration form) page to show some data grid with database data
See samples for each page enclosed!!

```html
<!DOCTYPE html>
<html lang="en">
<head>
<meta charset="utf-8">
<title>VORELT Portal – Grid Styling</title>
<link href="https://fonts.googleapis.com/css2?family=Ubuntu:wght@400;500;700&display=swap" rel="stylesheet">
<style>
:root{
  --navy:#0c2c47;
  --navy-hover:#15395a;
  --panel:#e1e6ea;
  --page:#f7f8f9;
  --line:#cfd6dc;
  --text:#2f3a44;
  --muted:#5c6670;
  --row-alt:#ebf6fb;
  --active-page:#b5b9bd;
  --white:#ffffff;
}
*{box-sizing:border-box;margin:0;padding:0}
html,body{width:1200px;height:948px;overflow:hidden}
body{font-family:"Ubuntu",sans-serif;color:var(--text);background:var(--page);position:relative}

.topbar{position:absolute;left:0;top:0;width:1200px;height:138px;background:var(--panel);border-bottom:1px solid #c4ccd3}
.brand{position:absolute;left:19px;top:48px;font-size:44px;font-weight:700;color:var(--navy);letter-spacing:1px}
.user{position:absolute;right:110px;top:50px;text-align:right}
.user-name{font-size:20px;font-weight:500;color:var(--navy)}
.user-role{font-size:14px;color:var(--muted);margin-top:1px}
.avatar{position:absolute;left:1100px;top:36px;width:66px;height:66px;border-radius:50%;background:linear-gradient(135deg,#8a8f93,#3e4245);border:2px solid #cfd5da}
.user-caret{position:absolute;left:1173px;top:64px}

.sidebar{position:absolute;left:11px;top:138px;width:265px;height:708px;background:var(--panel)}
.nav-item{position:absolute;left:0;width:265px;height:61px;display:flex;align-items:center;padding-left:20px;font-size:19px;color:var(--navy);border-bottom:1px solid #cbd2d8}
.nav-item svg{width:26px;height:26px;margin-right:12px;fill:var(--navy)}
.nav-item.is-open{background:var(--navy);color:var(--white);width:588px;border-bottom:none}
.nav-item.is-open svg{fill:var(--white)}
.nav-chevron{position:absolute;left:228px;top:23px}

.flyout{position:absolute;left:275px;top:384px;width:323px;height:192px;background:var(--navy);z-index:5}
.flyout-item{height:55px;display:flex;align-items:center;padding-left:29px;color:var(--white);font-size:19px;border-bottom:1px solid #08233a}
.flyout-item.is-hover{background:var(--navy-hover);height:53px}

.page-title{position:absolute;left:304px;top:186px;font-size:24px;font-weight:400;color:#3d4750}

.grid{position:absolute;border:1px solid var(--line);background:var(--white);border-collapse:collapse;font-size:14px}
.grid th{background:var(--panel);font-weight:400;font-size:17px;color:var(--text);text-align:left;padding-left:14px;border-right:1px solid var(--line)}
.grid td{color:var(--muted);padding-left:14px;border-top:1px solid var(--line);border-right:1px solid var(--line)}
.records{left:304px;top:228px;width:870px}
.records th{height:38px}
.records td{height:41px}
.check{width:14px;height:14px;border:1px solid #9aa3aa;background:#f1f3f5;display:inline-block;vertical-align:middle}
.pager-row td{height:62px;position:relative}
.per-page{position:absolute;left:279px;top:22px;font-size:14px;color:var(--muted)}
.pager{position:absolute;left:396px;top:11px;display:flex;align-items:center;height:37px;background:var(--white);border:1px solid #e2e6e9}
.pager-btn{background:var(--navy);color:var(--white);font-weight:700;font-size:13px;height:37px;width:63px;display:flex;align-items:center;justify-content:center;border-radius:2px}
.pager-pages{display:flex;align-items:center;width:337px;padding-left:28px;gap:0;font-size:14px;color:var(--text)}
.pager-pages span{padding:0 5px;line-height:37px}
.pager-pages .is-current{background:var(--active-page);color:var(--white)}

.approvals{left:304px;top:590px;width:417px}
.approvals th{height:38px}
.approvals td{height:36px}
.approvals tr:nth-child(even) td{background:var(--row-alt)}

.footer{position:absolute;left:0;top:887px;width:1200px;height:61px;background:var(--white);border-top:2px solid #eceff1;font-size:17px;color:#4a545d}
.copyright{position:absolute;left:14px;top:19px}
.footer-links{position:absolute;right:24px;top:19px}
</style>
</head>
<body>

<header class="topbar">
  <div class="brand">VORELT</div>
  <div class="user">
    <div class="user-name">Lars Brenner</div>
    <div class="user-role">Gest User</div>
  </div>
  <div class="avatar" role="img" aria-label="User profile photo"></div>
  <svg class="user-caret" width="11" height="7" viewBox="0 0 11 7"><path d="M0 0h11L5.5 7z" fill="#6b747c"/></svg>
</header>

<nav class="sidebar">
  <div class="nav-item" style="top:0">
    <svg viewBox="0 0 24 24"><path d="M3 5h15v14H4a1 1 0 0 1-1-1zm15 4h3v9a1 1 0 0 1-2 0h-1zM6 8h9v2H6zm0 4h9v1.5H6zm0 3h9v1.5H6z"/></svg>My News</div>
  <div class="nav-item" style="top:61px">
    <svg viewBox="0 0 24 24"><circle cx="10" cy="7" r="5"/><path d="M1 22c0-6 4-9 9-9 3 0 5 1 6 3v6z"/><circle cx="19" cy="19" r="3"/></svg>My User Settings</div>
  <div class="nav-item" style="top:122px">
    <svg viewBox="0 0 24 24"><circle cx="8" cy="8" r="5"/><circle cx="17" cy="16" r="4"/><circle cx="8" cy="8" r="2" fill="#e1e6ea"/><circle cx="17" cy="16" r="1.5" fill="#e1e6ea"/></svg>Company Settings</div>
  <div class="nav-item" style="top:183px">
    <svg viewBox="0 0 24 24"><path d="M3 19l9-9 2 2-9 9zM14 3a5 5 0 0 1 6 6l-3-1-2-2z"/><path d="M4 4l3 0 8 8-2 2-8-8z"/></svg>Configuration</div>
  <div class="nav-item is-open" style="top:246px">
    <svg viewBox="0 0 24 24"><path d="M2 4h4v4H2zm6 0h14v4H8zM2 10h4v4H2zm6 0h14v4H8zM2 16h4v4H2zm6 0h14v4H8z"/></svg>Services
    <svg class="nav-chevron" width="8" height="12" viewBox="0 0 8 12"><path d="M1 1l5 5-5 5" stroke="#fff" stroke-width="2" fill="none"/></svg></div>
  <div class="nav-item" style="top:290px">
    <svg viewBox="0 0 24 24"><path d="M12 4c5 0 9 3 9 7s-4 7-9 7l-7 3 2-4c-2-1-4-3-4-6 0-4 4-7 9-7z"/></svg>Communication</div>
  <div class="nav-item" style="top:351px;border-bottom:none">
    <svg viewBox="0 0 24 24"><path d="M4 5h8v2H6v11h11v-6h2v8H4z"/><path d="M13 3h8v8l-3-3-6 6-2-2 6-6z"/></svg>Logout</div>
</nav>

<div class="flyout">
  <div class="flyout-item is-hover">ZMS</div>
  <div class="flyout-item">DMS</div>
  <div class="flyout-item">REMS</div>
</div>

<h1 class="page-title">Grid Styling</h1>

<table class="grid records">
  <tr>
    <th style="width:56px;text-align:center;padding:0"><span class="check"></span></th>
    <th style="width:160px">Record</th>
    <th style="width:120px">Batch ID</th>
    <th style="width:204px">Keyword</th>
    <th style="width:108px">Status</th>
    <th>Reason</th>
  </tr>
  <tr><td style="text-align:center;padding:0"><span class="check"></span></td><td>Kamran</td><td>Yes</td><td>Some Dummy Text</td><td>Rejected</td><td>Policy Error: (adult)</td></tr>
  <tr><td style="text-align:center;padding:0"><span class="check"></span></td><td>Kamran</td><td>Yes</td><td>Some Dummy Text</td><td>Rejected</td><td>Policy Error: (adult)</td></tr>
  <tr><td style="text-align:center;padding:0"><span class="check"></span></td><td>Kamran</td><td>Yes</td><td>Some Dummy Text</td><td>Rejected</td><td>Policy Error: (adult)</td></tr>
  <tr><td style="text-align:center;padding:0"><span class="check"></span></td><td>Kamran</td><td>Yes</td><td>Some Dummy Text</td><td>Rejected</td><td>Policy Error: (adult)</td></tr>
  <tr class="pager-row"><td colspan="6" style="border-right:none">
    <span class="per-page">10 per page</span>
    <div class="pager">
      <div class="pager-btn">FIRST</div>
      <div class="pager-pages">
        <span class="is-current">1</span><span>2</span><span>3</span><span>4</span><span>5</span><span>6</span><span>7</span><span>8</span><span>9</span><span>10</span><span>....</span><span>100</span>
      </div>
      <div class="pager-btn">LAST</div>
    </div>
  </td></tr>
</table>

<table class="grid approvals">
  <tr><th style="width:72px">ID</th><th style="width:204px">Name</th><th>Approved</th></tr>
  <tr><td>201</td><td>Kamran</td><td>Yes</td></tr>
  <tr><td>202</td><td>Farid</td><td>No</td></tr>
  <tr><td>203</td><td>Tariq</td><td>Yes</td></tr>
  <tr><td>204</td><td>Imran</td><td>No</td></tr>
</table>

<footer class="footer">
  <div class="copyright">© 2016 VORELT. All rights reserved.</div>
  <div class="footer-links">Help &nbsp;/&nbsp; Disclaimer &nbsp;/&nbsp; Contact</div>
</footer>

</body>
</html>
```